Waste management company seeks a new website design

We need a website design for an environmental services company called 'Vilumetsa Kogumisteenused.' We manage waste collection and recycling for 100K+ households and businesses across Estonia. Please use logos and colors from attached CVI file. The design should be extensively usable for our self-service portal and have a mobile-first approach as it will be turned into an app in the future. The new website should highlight our commitment to sustainability and provide easy access to our services with a clean, modern design. UX inspiration from https://trevix.eu/et-ee/

```html
<!DOCTYPE html>
<html lang="en">
<head>
<meta charset="utf-8">
<title>Vilumetsa Kogumisteenused</title>
<link href="https://fonts.googleapis.com/css2?family=Inter:wght@400;500;600&display=swap" rel="stylesheet">
<style>
:root{
  --lime:#d4dc44;
  --plum:#7b5e63;
  --text:#6e575c;
  --card:#f3f2f1;
  --grey:#d7d4d6;
  --line:#ebe8e8;
  --white:#ffffff;
}
*{margin:0;padding:0;box-sizing:border-box}
html,body{width:1200px;height:3943px;overflow:hidden;background:var(--white)}
body{position:relative;font-family:'Inter',sans-serif;color:var(--text)}
.abs{position:absolute}
a{color:inherit;text-decoration:none}
.site-header{position:absolute;left:0;top:0;width:1200px;height:90px;z-index:5}
.btn{position:absolute;display:flex;align-items:center;justify-content:center;border-radius:22px;font-size:13px;font-weight:500}
.btn-lime{background:var(--lime);color:var(--white)}
.btn-grey{background:var(--grey);color:var(--white)}
.btn-white{background:var(--white);color:var(--plum)}
.brand{position:absolute;display:flex;align-items:center;gap:8px;color:var(--plum);font-weight:500}
.brand-dot{border-radius:50%;background:var(--lime)}
h1,h2,h3{font-weight:500;color:var(--plum)}
.section-title{position:absolute;left:0;width:1200px;text-align:center;font-size:42px}
.section-sub{position:absolute;left:0;width:1200px;text-align:center;font-size:13px}
.photo{position:absolute;border-radius:10px}
.hero-photo{position:absolute;left:230px;top:0;width:970px;height:700px;border-bottom-right-radius:420px;
  background:linear-gradient(90deg,#ffffff 0%,#f1e8df 30%,#d9c4b2 60%,#c9ae97 100%)}
.hero-title{position:absolute;left:67px;top:212px;font-size:43px;line-height:54px;z-index:2}
.hero-text{position:absolute;left:67px;top:347px;width:455px;font-size:13px;line-height:21px;z-index:2}
.service-card{position:absolute;top:938px;width:525px;height:257px;background:var(--card);border-radius:16px;overflow:hidden}
.service-card h3{position:absolute;left:42px;top:80px;font-size:20px}
.service-card p{position:absolute;left:42px;top:118px;width:230px;font-size:12.5px;line-height:21px}
.service-art{position:absolute;right:20px;bottom:0;width:220px;height:200px;background:var(--lime);border-radius:20px 20px 0 0;opacity:.9}
.about-title{position:absolute;left:67px;top:1355px;font-size:42px}
.about-text{position:absolute;left:67px;top:1428px;width:525px;font-size:12.5px;line-height:21px}
.stat{position:absolute;left:67px}
.stat .tick{position:absolute;left:0;top:4px;width:20px;height:20px;border-radius:50%;background:var(--lime)}
.stat .tick svg{position:absolute;left:5px;top:6px}
.stat strong{position:absolute;left:43px;top:0;font-size:20px;font-weight:500;color:var(--plum);white-space:nowrap}
.stat span{position:absolute;left:43px;top:32px;width:360px;font-size:12.5px;line-height:21px}
.app-card{position:absolute;left:67px;top:2183px;width:1066px;height:505px;background:var(--lime);border-radius:18px;overflow:hidden}
.app-card h2{position:absolute;left:72px;top:124px;font-size:42px;line-height:54px;color:var(--white)}
.app-card p{position:absolute;left:72px;top:260px;width:450px;font-size:12.5px;line-height:21px;color:var(--white)}
.app-visual{position:absolute;left:637px;top:44px;width:400px;height:461px;border-radius:30px 30px 0 0;background:linear-gradient(160deg,#ffffff 0%,#f1e6d8 45%,#d8bea3 100%)}
.news-title{position:absolute;left:67px;top:2848px;font-size:42px}
.news-card{position:absolute;top:2940px;width:344px}
.news-card .photo{left:0;top:0;width:344px;height:208px}
.news-card h3{position:absolute;left:0;top:248px;width:300px;font-size:26px;line-height:33px}
.news-card time{position:absolute;left:0;top:328px;font-size:12.5px}
.footer-col{position:absolute;top:3489px}
.footer-col h4{font-size:20px;font-weight:500;color:var(--plum);margin-bottom:22px}
.footer-col li{list-style:none;font-size:12.5px;height:36px}
.lang{position:absolute;display:flex;align-items:center;gap:6px;font-size:12px}
.social{position:absolute;top:3779px;width:26px;height:26px;border-radius:50%;background:var(--grey)}
.footer-rule{position:absolute;left:67px;top:3832px;width:1066px;height:1px;background:var(--line)}
.legal{position:absolute;top:3860px;font-size:12.5px}
</style>
</head>
<body>

<section class="hero">
  <div class="hero-photo" role="img" aria-label="Woman with closed eyes enjoying the breeze by the water at sunset"></div>
  <h1 class="hero-title">Hoolime loodusest,<br>hoolime tulevikust</h1>
  <p class="hero-text">Lorem ipsum dolor sit amet consectetur. Volutpat ac arcu sed aliquam eu. Pellentesque pulvinar posuere felis platea a nullam imperdiet nunc. Lacus iaculis euismod phasellus duis pretium eget id. Elit at sed sit enim aliquet.</p>
  <a class="btn btn-lime" style="left:67px;top:456px;width:158px;height:42px;z-index:2">Get the app</a>
</section>

<header class="site-header">
  <div class="brand" style="left:70px;top:36px;font-size:12px;line-height:13px">
    <span class="brand-dot" style="width:24px;height:24px"></span>
    <span>Vilumetsa<br>Kogumisteenused</span>
  </div>
  <div class="lang" style="left:780px;top:38px;color:var(--white)">
    <svg width="16" height="16" viewBox="0 0 16 16" fill="none" stroke="#fff" stroke-width="1.2"><circle cx="8" cy="8" r="6.5"/><ellipse cx="8" cy="8" rx="3" ry="6.5"/><path d="M1.5 8h13"/></svg>EN
  </div>
  <a class="abs" style="left:868px;top:38px;font-size:13px;color:var(--white);font-weight:500">Support</a>
  <a class="btn btn-lime" style="left:947px;top:30px;width:132px;height:31px">Sign up</a>
  <svg class="abs" style="left:1110px;top:38px" width="20" height="16" viewBox="0 0 20 16" stroke="#fff" stroke-width="1.5"><path d="M0 2h20M0 8h20M0 14h20"/></svg>
</header>

<section class="services">
  <h2 class="section-title" style="top:808px">Our services</h2>
  <p class="section-sub" style="top:882px">Lorem ipsum dolor sit amet consectetur. Aliquam fames gravida augue in tempor vel.</p>
  <article class="service-card" style="left:67px">
    <h3>Waste collection</h3>
    <p>Lorem ipsum dolor sit amet consectetur. Aliquam fames gravida augue in tempor vel.</p>
    <div class="service-art" role="img" aria-label="Waste bin illustration"></div>
  </article>
  <article class="service-card" style="left:608px">
    <h3>Recycling</h3>
    <p>Lorem ipsum dolor sit amet consectetur. Aliquam fames gravida augue in tempor vel.</p>
    <div class="service-art" role="img" aria-label="Recycling arrows illustration"></div>
  </article>
</section>

<section class="about">
  <h2 class="about-title">About us</h2>
  <p class="about-text">Vilumetsa Kogumisteenused is a leading group of waste management and utilities in Estonia, the main activity of which is the collection of municipal waste. In addition, the company is engaged in the collection of secondary raw materials, construction waste. In some areas, the company also offers road and streets in the winter. The company is serving</p>

  <div class="stat" style="top:1550px"><span class="tick"><svg width="10" height="8" viewBox="0 0 10 8" fill="none" stroke="#fff" stroke-width="1.8"><path d="M1 4l3 3 5-6"/></svg></span><strong>100,000+</strong><span>Customers around Estonia.</span></div>
  <div class="stat" style="top:1620px"><span class="tick"><svg width="10" height="8" viewBox="0 0 10 8" fill="none" stroke="#fff" stroke-width="1.8"><path d="M1 4l3 3 5-6"/></svg></span><strong>250,000+</strong><span>Tons of wastes</span></div>
  <div class="stat" style="top:1690px"><span class="tick"><svg width="10" height="8" viewBox="0 0 10 8" fill="none" stroke="#fff" stroke-width="1.8"><path d="M1 4l3 3 5-6"/></svg></span><strong>600+</strong><span>employee</span></div>
  <div class="stat" style="top:1760px"><span class="tick"><svg width="10" height="8" viewBox="0 0 10 8" fill="none" stroke="#fff" stroke-width="1.8"><path d="M1 4l3 3 5-6"/></svg></span><strong>ISO9001, ISO14001 and ISO45001</strong><span>integrated occupational health, safety, quality and environmental management system</span></div>

  <a class="btn btn-grey" style="left:67px;top:1853px;width:156px;height:42px">Learn more</a>

  <div class="photo" style="left:879px;top:1355px;width:254px;height:125px;background:linear-gradient(120deg,#6b5a52,#c49a6a 55%,#e0b77c)" role="img" aria-label="Person in a knit hat in an autumn forest"></div>
  <div class="photo" style="left:608px;top:1502px;width:525px;height:183px;background:linear-gradient(100deg,#3f3a22,#a88a3e 45%,#e6c26b 70%,#6f6230)" role="img" aria-label="Tall grass backlit by golden sunlight"></div>
  <div class="photo" style="left:608px;top:1705px;width:254px;height:127px;background:linear-gradient(180deg,#d7aa98 0%,#e4b89c 50%,#5b4a55 100%)" role="img" aria-label="Old town skyline with church spire at dusk"></div>
</section>

<section class="apps">
  <h2 class="section-title" style="top:2054px">Download our apps</h2>
  <p class="section-sub" style="top:2127px">Lorem ipsum dolor sit amet consectetur. Aliquam fames gravida augue in tempor vel.</p>
  <div class="app-card">
    <h2>Lorem ipsum dolor sit<br>amet consectetur.</h2>
    <p>Lorem ipsum dolor sit amet consectetur. Interdum habitant cras cursus dui scelerisque felis quam bibendum enim. Ipsum viverra quam sit pretium sollicitudin euismod.</p>
    <a class="btn btn-white" style="left:72px;top:344px;width:159px;height:41px">Get the app</a>
    <div class="app-visual" role="img" aria-label="Wooden hand holding a smartphone showing the app start screen"></div>
  </div>
</section>

<section class="news">
  <h2 class="news-title">News and updates</h2>
  <a class="btn btn-grey" style="left:999px;top:2852px;width:134px;height:41px">View all</a>
  <article class="news-card" style="left:67px">
    <div class="photo" style="background:linear-gradient(135deg,#4a4740,#b9623f 45%,#7d7468)" role="img" aria-label="Aerial view of red-roofed old town"></div>
    <h3>Lorem ipsum dolor sit amet consectetur.</h3>
    <time>12/01/2024</time>
  </article>
  <article class="news-card" style="left:427px">
    <div class="photo" style="background:linear-gradient(180deg,#8fb4cf 0%,#2b3236 45%,#d9583a 70%,#5b7c8f 100%)" role="img" aria-label="Ship bow in icy harbour with a flag"></div>
    <h3>Lorem ipsum dolor sit amet consectetur.</h3>
    <time>12/01/2024</time>
  </article>
  <article class="news-card" style="left:788px">
    <div class="photo" style="background:linear-gradient(180deg,#f4c24f 0%,#e8a232 50%,#8a6a25 100%)" role="img" aria-label="Lone pine tree in a misty golden meadow"></div>
    <h3>Lorem ipsum dolor sit amet consectetur.</h3>
    <time>12/01/2024</time>
  </article>
</section>

<footer>
  <div class="brand" style="left:73px;top:3450px;font-size:18px;line-height:20px">
    <span class="brand-dot" style="width:40px;height:40px"></span>
    <span>Vilumetsa<br>Kogumisteenused</span>
  </div>
  <div class="lang" style="left:78px;top:3533px">
    <svg width="16" height="16" viewBox="0 0 16 16" fill="none" stroke="#6e575c" stroke-width="1.2"><circle cx="8" cy="8" r="6.5"/><ellipse cx="8" cy="8" rx="3" ry="6.5"/><path d="M1.5 8h13"/></svg>EN
    <svg width="8" height="6" viewBox="0 0 8 6" fill="none" stroke="#bbb" stroke-width="1.2"><path d="M1 1l3 3 3-3"/></svg>
  </div>
  <div class="footer-col" style="left:427px"><h4>Services</h4><ul><li>waste collection</li><li>recycling</li></ul></div>
  <div class="footer-col" style="left:653px"><h4>Support</h4><ul><li>Client support</li><li>General Conditions</li><li>Get the app</li></ul></div>
  <div class="footer-col" style="left:879px"><h4>Company</h4><ul><li>About Us</li><li>Careers</li><li>Green plan</li><li>Blog</li><li>Contact us</li></ul></div>

  <span class="social" style="left:966px"></span>
  <span class="social" style="left:1001px"></span>
  <span class="social" style="left:1036px"></span>
  <span class="social" style="left:1071px"></span>
  <span class="social" style="left:1106px"></span>

  <div class="footer-rule"></div>
  <p class="legal" style="left:67px">© 2024 vilumetsa kogumisteenused</p>
  <a class="legal" style="left:695px">Suppliers</a>
  <a class="legal" style="left:781px">Terms &amp; Conditions</a>
  <a class="legal" style="left:930px">Privacy</a>
  <a class="legal" style="left:1004px">Cookies</a>
  <a class="legal" style="left:1081px">Security</a>
</footer>

</body>
</html>
```